Banner to celebrate Pellister Journeys 40 years in business. Will be used on our social media channels.

Hello
We would like a banner created to celebrate 40 years in business with tagline "service through experience since 1983"
also add our website pellisterjourneys.com.au
Banner size must be : 650 x 150px
open to suggestions

Target Market(s)

current and prospective clients

Industry/Entity Type

Travel & Tourism (Business Travel)

Colors
0054AA
0677BA
7BADD7
CADEEF
E8F1F8

Requirements
Must have
• use current theme of our website www.pellisterjourneys.com.au. Keep simple and effective.
Nice to have
• use one image that I have provided
Should not have
• multiple graphics

```html
<!DOCTYPE html>
<html lang="en">
<head>
<meta charset="utf-8">
<title>Pellister Journeys – 40 Years in Business Banners</title>
<link href="https://fonts.googleapis.com/css2?family=Arimo:wght@400;700&display=swap" rel="stylesheet">
<style>
  :root{
    --navy:#1f4a85;
    --blue:#0054aa;
    --blue-mid:#0677ba;
    --sky:#7badd7;
    --ice:#e8f1f8;
    --gold:#d2bb80;
    --ink:#3a3a3a;
    --dark:#1c1c1e;
  }
  *{box-sizing:border-box;margin:0;padding:0}
  html,body{width:1200px;height:857px;overflow:hidden;background:#fff}
  body{position:relative;font-family:"Arimo",Arial,sans-serif}

  .banner{position:absolute;width:557px;height:129px;overflow:hidden}
  .photo{position:absolute;top:0;bottom:0}

  /* anniversary wording, plain text */
  .milestone{position:absolute;color:var(--gold);font-weight:700;white-space:nowrap;line-height:1}
  .milestone .num{display:inline-block}
  .milestone .unit{display:inline-block}
  .milestone .label{display:block}

  /* ---------- side-panel style ---------- */
  .panel{position:absolute;left:0;top:0;width:137px;height:100%;background:var(--navy)}
  .panel .brand{position:absolute;left:19px;top:13px;color:#fff;font-weight:700;font-size:13px;white-space:nowrap}
  .panel .milestone{left:19px;top:44px}
  .panel .milestone .num{font-size:48px;letter-spacing:-1px}
  .panel .milestone .unit{font-size:12px;margin-left:4px}
  .panel .milestone .label{font-size:12.5px;margin-top:14px}
  .side .photo{left:137px;right:0}

  .tagline{position:absolute;text-align:right;right:19px;top:28px;color:var(--ink)}
  .tagline .lead{font-size:12.5px;letter-spacing:.1px}
  .tagline .main{font-size:18px;letter-spacing:.3px;margin-top:1px}
  .tagline .since{font-size:11.5px;letter-spacing:2.5px;margin-top:3px}
  .tagline .url{position:absolute;right:0;top:74px;font-weight:700;font-size:11px;color:var(--navy);white-space:nowrap}
  .side.dark .tagline{color:#fff}
  .side.dark .tagline .url{color:var(--gold)}

  /* ---------- full-bleed style ---------- */
  .wide{background:var(--dark)}
  .wide .photo{left:0;right:0}
  .wide .milestone{left:13px;top:24px}
  .wide .milestone .num{font-size:72px;letter-spacing:-2px}
  .wide .milestone .unit{font-size:16px;margin-left:6px}
  .wide .milestone .label{font-size:18px;margin-top:7px}
  .wide .tagline{left:171px;right:auto;top:44px;text-align:left;color:#fff}
  .wide .tagline .lead{font-size:14px}
  .wide .tagline .main{font-size:21px}
  .wide .tagline .since{font-size:13px}
  .wide .signoff{position:absolute;right:15px;top:62px;text-align:right}
  .wide .signoff .brand{font-weight:700;font-size:16px;color:var(--navy);white-space:nowrap}
  .wide .signoff .url{font-weight:700;font-size:11px;color:var(--navy);margin-top:8px}

  .l1{left:30px;top:47px}.l2{left:30px;top:206px}.l3{left:30px;top:364px}.l4{left:30px;top:523px}.l5{left:30px;top:681px}
  .r1{left:613px;top:47px}.r2{left:613px;top:206px}.r3{left:613px;top:364px}.r4{left:613px;top:523px}
</style>
</head>
<body>

<section class="banner side l1">
  <div class="panel"><span class="brand">Pellister Journeys</span><p class="milestone"><span class="num">40</span><span class="unit">YEARS</span><span class="label">IN BUSINESS</span></p></div>
  <div class="photo" role="img" aria-label="Businessman walking through an airport terminal with a suitcase" style="background:linear-gradient(90deg,#8a857c,#c9c4bb 45%,#efede9 75%,#f7f6f4)"></div>
  <div class="tagline"><p class="lead">SERVICE THROUGH</p><p class="main">EXPERIENCE</p><p class="since">— since 1983 —</p><p class="url">pellisterjourneys.com.au</p></div>
</section>

<section class="banner side dark l2">
  <div class="panel"><span class="brand">Pellister Journeys</span><p class="milestone"><span class="num">40</span><span class="unit">YEARS</span><span class="label">IN BUSINESS</span></p></div>
  <div class="photo" role="img" aria-label="Two colleagues reviewing a tablet in an office with timber slats" style="background:linear-gradient(90deg,#5f6b74,#4a3d33 45%,#2a1f18 75%,#1d1511)"></div>
  <div class="tagline"><p class="lead">SERVICE THROUGH</p><p class="main">EXPERIENCE</p><p class="since">— since 1983 —</p><p class="url">pellisterjourneys.com.au</p></div>
</section>

<section class="banner side l3">
  <div class="panel"><span class="brand">Pellister Journeys</span><p class="milestone"><span class="num">40</span><span class="unit">YEARS</span><span class="label">IN BUSINESS</span></p></div>
  <div class="photo" role="img" aria-label="Travel consultant smiling while meeting a client in a bright lounge" style="background:linear-gradient(90deg,#a9826a,#e7dccf 40%,#eef1f4 70%,#f1f3f6)"></div>
  <div class="tagline"><p class="lead">SERVICE THROUGH</p><p class="main">EXPERIENCE</p><p class="since">— since 1983 —</p><p class="url">pellisterjourneys.com.au</p></div>
</section>

<section class="banner side dark l4">
  <div class="panel"><span class="brand">Pellister Journeys</span><p class="milestone"><span class="num">40</span><span class="unit">YEARS</span><span class="label">IN BUSINESS</span></p></div>
  <div class="photo" role="img" aria-label="Two travel consultants with headsets at a reception desk" style="background:linear-gradient(90deg,#3b3836,#7b6a5d 35%,#5a3e2b 65%,#3c2819)"></div>
  <div class="tagline"><p class="lead">SERVICE THROUGH</p><p class="main">EXPERIENCE</p><p class="since">— since 1983 —</p><p class="url">pellisterjourneys.com.au</p></div>
</section>

<section class="banner side l5">
  <div class="panel"><span class="brand">Pellister Journeys</span><p class="milestone"><span class="num">40</span><span class="unit">YEARS</span><span class="label">IN BUSINESS</span></p></div>
  <div class="photo" role="img" aria-label="Team of travel consultants working together at a computer" style="background:linear-gradient(90deg,#7f96ad,#c9cfd6 40%,#e6ebf0 70%,#edf1f5)"></div>
  <div class="tagline"><p class="lead">SERVICE THROUGH</p><p class="main">EXPERIENCE</p><p class="since">— since 1983 —</p><p class="url">pellisterjourneys.com.au</p></div>
</section>

<section class="banner wide r1">
  <div class="photo" role="img" aria-label="Traveller pulling a suitcase through an airport concourse" style="background:linear-gradient(90deg,#1d1a18 25%,#4f463e 55%,#a39c93 80%,#e9e8e6)"></div>
  <p class="milestone"><span class="num">40</span><span class="unit">YEARS</span><span class="label">IN BUSINESS</span></p>
  <div class="tagline"><p class="lead">SERVICE THROUGH</p><p class="main">EXPERIENCE</p><p class="since">— since 1983 —</p></div>
  <div class="signoff"><p class="brand">Pellister Journeys</p><p class="url">pellisterjourneys.com.au</p></div>
</section>

<section class="banner wide r2">
  <div class="photo" role="img" aria-label="Business travellers walking through an airport terminal" style="background:linear-gradient(90deg,#1b1a1a 25%,#3f3c3a 50%,#9a9896 75%,#ecebea)"></div>
  <p class="milestone"><span class="num">40</span><span class="unit">YEARS</span><span class="label">IN BUSINESS</span></p>
  <div class="tagline"><p class="lead">SERVICE THROUGH</p><p class="main">EXPERIENCE</p><p class="since">— since 1983 —</p></div>
  <div class="signoff"><p class="brand">Pellister Journeys</p><p class="url">pellisterjourneys.com.au</p></div>
</section>

<section class="banner wide r3">
  <div class="photo" role="img" aria-label="Smiling businesswoman using her phone in a city street" style="background:linear-gradient(90deg,#1f2a2c 25%,#3f4f52 50%,#8c9799 75%,#e7ebec)"></div>
  <p class="milestone"><span class="num">40</span><span class="unit">YEARS</span><span class="label">IN BUSINESS</span></p>
  <div class="tagline"><p class="lead">SERVICE THROUGH</p><p class="main">EXPERIENCE</p><p class="since">— since 1983 —</p></div>
  <div class="signoff"><p class="brand">Pellister Journeys</p><p class="url">pellisterjourneys.com.au</p></div>
</section>

<section class="banner wide r4">
  <div class="photo" role="img" aria-label="Cheerful travel consultant wearing a headset" style="background:linear-gradient(90deg,#151313 25%,#3a2a24 45%,#7c5a45 60%,#bdb9b6 80%,#ecebea)"></div>
  <p class="milestone"><span class="num">40</span><span class="unit">YEARS</span><span class="label">IN BUSINESS</span></p>
  <div class="tagline"><p class="lead">SERVICE THROUGH</p><p class="main">EXPERIENCE</p><p class="since">— since 1983 —</p></div>
  <div class="signoff"><p class="brand">Pellister Journeys</p><p class="url">pellisterjourneys.com.au</p></div>
</section>

</body>
</html>
```